Velora Pedalworks

We are a new start up company selling (online) innovative cycling products.
Being a new player in the market a modern eye catching logo would be good.
Initially selling safety tail lights with blinkers & modern designed cycling gloves and eventually extending our range into cycling clothing. Many of our products will have a safety theme.

Please see logo attached.

Reason: I have extended deadline because i have just received the Logo to be used.

Target Market(s)

We will be target marketing to the young 20-30year old trendy commuter cyclists to the 40 - 60 year old weekend road riders with there immaculate color coordinated road bikes & clothing.

Industry/Entity Type

Safety

Requirements
Must have
• Name: Mavin Tolby
Line for Mobile No. 0438 261 905
Line for email Address: mavin@velorapedalworks.example.com.au
3 Lines for Postal Address: PO Box 3862
Wattle Crest Corner
NSW 2174
Website: www.velorapedalworks.example.com.au

```html
<!DOCTYPE html>
<html lang="en">
<head>
<meta charset="utf-8">
<title>Velora Pedalworks — Business Card</title>
<link rel="stylesheet" href="https://fonts.googleapis.com/css2?family=Mukta:wght@400;700&display=swap">
<style>
  :root {
    --page-bg: #eef0f3;
    --card-bg: #ffffff;
    --card-edge: #d6d8dc;
    --ink: #111111;
    --accent-orange: #f47a12;
    --rule-yellow: #f5c518;
  }
  html, body {
    margin: 0;
    padding: 0;
    width: 1200px;
    height: 1000px;
    overflow: hidden;
    background: var(--page-bg);
    font-family: "Mukta", sans-serif;
  }
  .business-card {
    position: absolute;
    left: 240px;
    top: 293px;
    width: 720px;
    height: 416px;
    background: var(--card-bg);
    border: 1px solid var(--card-edge);
    border-radius: 18px;
    box-sizing: border-box;
  }
  .brand {
    position: absolute;
    left: 40px;
    top: 108px;
    display: flex;
    align-items: center;
    gap: 10px;
  }
  .brand-dot {
    width: 18px;
    height: 18px;
    border-radius: 50%;
    background: var(--accent-orange);
  }
  .brand-name {
    font-size: 36px;
    font-weight: 400;
    color: var(--ink);
    line-height: 1;
    letter-spacing: -0.3px;
  }
  .divider-rule {
    position: absolute;
    left: 14px;
    right: 14px;
    top: 164px;
    height: 2px;
    background: var(--rule-yellow);
  }
  .contact {
    position: absolute;
    right: 27px;
    top: 175px;
    text-align: right;
    color: var(--ink);
  }
  .contact-name {
    font-size: 24px;
    font-weight: 700;
    line-height: 1;
    margin: 0 0 40px;
  }
  .contact-lines {
    font-size: 18px;
    line-height: 23px;
    margin: 0;
  }
  .contact-lines + .contact-lines {
    margin-top: 11px;
  }
</style>
</head>
<body>
  <div class="business-card">
    <div class="brand">
      <span class="brand-dot"></span>
      <span class="brand-name">Velora Pedalworks</span>
    </div>
    <div class="divider-rule"></div>
    <div class="contact">
      <p class="contact-name">Mavin Tolby</p>
      <p class="contact-lines">
        0438 261 905<br>
        mavin@velorapedalworks.example.com.au
      </p>
      <p class="contact-lines">
        PO Box 3862<br>
        Wattle Crest Corner<br>
        NSW 2174<br>
        www.velorapedalworks.example.com.au
      </p>
    </div>
  </div>
</body>
</html>
```